PALMERA corporate branding Powerpoint template*

We are a IT / tech company focussed on no nonsense services for our customers. Our main colors are blue and Orange as seen in the attached logo. Our catchphrase is It's palmera. We will use this template for corporate presentations at customers and potential projects.Please make sure the powerpoint does not have any art in there as the standard computers or whatsoever. We want a sleek clean design with our logo and both our colors in a main role.

Target Market(s)

Our existing customers and new customers

Industry/Entity Type

It Company

Colors

Designer to choose colors to be used in the design.

Requirements
Must have
• Different slides for different scenarios.
• Look and feel across the entire template
Nice to have
• Enough space to have our own bullet points
Should not have
• To overcrowded slides. Too loud design.

```html
<!DOCTYPE html>
<html lang="en">
<head>
<meta charset="utf-8">
<title>PALMERA corporate presentation template</title>
<link href="https://fonts.googleapis.com/css2?family=Bebas+Neue&family=Oswald:wght@300;400&family=Open+Sans:wght@400;700;800&display=swap" rel="stylesheet">
<style>
:root{
  --orange:#f26a10;
  --blue:#1f4e8f;
  --slate:#4a5468;
  --head-grey:#a4a4a4;
  --slide-bg:#f3f3f3;
  --page-bg:#ffffff;
  --ink:#555a60;
  --dark-panel:#3e3e3e;
  --rule:#f5a46e;
}
*{box-sizing:border-box;margin:0;padding:0}
html,body{width:1200px;height:2201px;overflow:hidden;background:var(--page-bg)}
body{position:relative;font-family:'Open Sans',Arial,sans-serif;color:var(--ink)}
.display{font-family:'Oswald','Arial Narrow',sans-serif;font-weight:300;text-transform:uppercase;letter-spacing:-.2px}
.poster{font-family:'Bebas Neue',Impact,sans-serif;font-weight:400}

/* ---------- title slide ---------- */
.title-slide{position:absolute;left:68px;top:50px;width:607px;height:343px;background:var(--slide-bg);box-shadow:0 2px 6px rgba(0,0,0,.25)}
.title-slide .brand{position:absolute;left:76px;top:88px}
.title-slide .brand-name{font-size:21px}
.title-main{position:absolute;left:74px;top:124px;font-size:64px;line-height:52px}
.title-main .t-orange{color:var(--orange);display:block}
.title-main .t-blue{color:var(--blue);display:block}
.title-rule{position:absolute;left:76px;top:228px;width:456px;border-top:1px dashed var(--rule)}
.title-byline{position:absolute;left:76px;top:236px;font-size:17px;color:var(--orange)}

/* ---------- feature list ---------- */
.features{position:absolute;left:756px;top:28px;width:440px;font-weight:800;font-size:21px;line-height:30px;color:#1c1c1c;list-style:none}
.features > li{position:relative;padding-left:26px}
.features > li::before{content:"";position:absolute;left:0;top:6px;width:17px;height:17px;border:2px solid #1c1c1c}
.features .sub{list-style:none;margin-left:44px;line-height:27px}
.features .sub li{position:relative;padding-left:17px}
.features .sub li::before{content:"";position:absolute;left:0;top:9px;width:7px;height:7px;background:#1c1c1c}

/* ---------- generic slide ---------- */
.slide{position:absolute;width:375px;height:212px;background:var(--slide-bg);box-shadow:1px 2px 5px rgba(0,0,0,.3);overflow:hidden}
.col-a{left:24px}.col-b{left:414px}.col-c{left:804px}
.row-1{top:482px}.row-2{top:775px}.row-3{top:1069px}.row-4{top:1362px}.row-5{top:1656px}.row-6{top:1950px}

.brand{position:absolute;line-height:1}
.brand-name{display:block;font-weight:700;color:var(--blue);font-size:12px;letter-spacing:.3px}
.slide .brand{right:22px;top:11px}

.slide-head{position:absolute;left:0;top:0;width:100%;height:31px;background:var(--head-grey);border-left:6px solid var(--orange)}
.slide-head .h-title{position:absolute;left:6px;top:3px;font-size:13px;color:#fff;line-height:1.1}
.slide-head .h-sub{position:absolute;left:6px;top:20px;font-size:5px;color:#fff;line-height:1}

.slide-foot{position:absolute;left:0;bottom:0;width:100%;height:10px;background:var(--slate)}
.slide-foot .page-no{position:absolute;right:130px;top:2px;font-size:5px;color:var(--orange);font-family:'Oswald',sans-serif;font-weight:300;text-transform:uppercase;line-height:1}
.slide-foot .page-no b{margin-left:18px;font-weight:300}
.slide-foot .foot-title{position:absolute;right:0;top:0;width:108px;height:10px;background:var(--orange);color:#fff;font-size:4.6px;font-family:'Oswald',sans-serif;font-weight:300;text-transform:uppercase;text-align:right;padding:2.6px 3px 0 0;line-height:1;white-space:nowrap}

.copy{font-size:4.6px;line-height:6.2px;color:var(--ink)}
.copy p+p{margin-top:4px}
.copy .hl{color:var(--orange)}
.label{font-family:'Oswald',sans-serif;font-weight:300;text-transform:uppercase;color:var(--orange);font-size:7px;line-height:1.1;border-bottom:1px dashed var(--rule);padding-bottom:1px;margin-bottom:3px;white-space:nowrap}

.section-title{position:absolute;left:96px;top:86px;width:279px}
.section-title .st-name{font-family:'Oswald',sans-serif;font-weight:300;text-transform:uppercase;font-size:14px;color:#3d3d3d;line-height:1.15;padding-bottom:2px;border-bottom:1px dashed var(--rule)}
.section-title .st-sub{font-family:'Oswald',sans-serif;font-weight:300;text-transform:uppercase;font-size:5px;color:var(--orange);margin-top:3px}

.photo{position:absolute}
.photo-cables{background:linear-gradient(135deg,#d9e3b0 0%,#7fc9c4 45%,#2f7f86 100%)}
.photo-servers{background:linear-gradient(90deg,#3a3a3a 0%,#9a9a9a 45%,#e2e2e2 70%,#bdbdbd 100%)}
.photo-rack{background:linear-gradient(160deg,#2b3a33 0%,#6d7f73 50%,#c9cfcb 100%)}
.photo-person{background:linear-gradient(160deg,#f2e6cf 0%,#d6a878 55%,#8a6a4a 100%)}
.photo-desk{background:linear-gradient(110deg,#dfe4e8 0%,#c3ccd3 45%,#3d4652 75%,#a8b0b8 100%)}

.orange{color:var(--orange)}
.bullets{list-style:disc;padding-left:7px}
.bullets li+li{margin-top:4px}
</style>
</head>
<body>

<!-- title slide -->
<section class="title-slide" aria-label="Title slide">
  <div class="brand"><span class="brand-name">PALMERA</span></div>
  <h1 class="title-main poster"><span class="t-orange">Business</span><span class="t-blue">Presentation</span></h1>
  <div class="title-rule"></div>
  <p class="title-byline display">Jane Sample Doe / Nov 2019</p>
</section>

<ul class="features">
  <li>Ratio 16:9</li>
  <li>Full HD</li>
  <li>Custom color pallet</li>
  <li>Custom Font -&nbsp; Easy Change</li>
  <li>Easy to edit, just drag and drop images</li>
  <li>Can be included up to 100 slides;
    <ul class="sub">
      <li>Text + images (1,2,3,4) , Text Slides</li>
      <li>Portfolio Slides , blog slides</li>
      <li>Text Slides, infographics</li>
      <li>Data Slides</li>
    </ul>
  </li>
  <li>In the sample you find 19 slides</li>
</ul>

<!-- row 1 -->
<section class="slide col-a row-1">
  <div class="brand"><span class="brand-name">PALMERA</span></div>
  <div class="section-title">
    <div class="st-name">About us</div>
    <div class="st-sub">A brief description here</div>
    <p class="display orange" style="font-size:5px;line-height:7px;margin-top:4px;width:262px">Lorem ipsum dolor sit amet lorem ipsum dolor sit amet lorem ipsum dolor sit amet lorem ipsum dolor sit amet lorem ipsum dolor sit amet lorem ipsum dolor sit amet lorem ipsum dolor sit amet lorem ipsum dolor sit amet lorem ipsum dolor sit amet lorem ipsum dolor sit amet lorem ipsum dolor sit amet lorem ipsum dolor sit amet lorem ipsum dolor sit amet lorem ipsum dolor sit amet lorem ipsum dolor sit amet lorem ipsum dolor sit amet lorem ipsum dolor sit amet lorem ipsum dolor sit amet</p>
  </div>
</section>

<section class="slide col-b row-1">
  <div class="slide-head"><span class="h-title display">Our vision</span><span class="h-sub display">Lorem ipsum dolor sit amet</span></div>
  <div class="brand"><span class="brand-name">PALMERA</span></div>
  <div class="display" style="position:absolute;left:64px;top:102px;font-size:15px;color:#3d3d3d">Our vision</div>
  <div style="position:absolute;left:0;top:122px;width:132px;height:2px;background:var(--orange)"></div>
  <ul class="copy bullets" style="position:absolute;left:148px;top:66px;width:212px">
    <li>Lorem ipsum dolor sit amet, consectetur adipisicing elit, sed do eiusmod tempor incididunt ut labore et dolore magna aliqua. Ut enim ad minim veniam, quis nostrud exercitation ullamco laboris nisi ut aliquip ex ea commodo consequat.</li>
    <li>Duis aute irure dolor in reprehenderit in voluptate velit esse cillum dolore eu fugiat nulla pariatur. Excepteur sint occaecat cupidatat non proident, sunt in culpa qui officia deserunt mollit anim id est laborum.</li>
    <li>Lorem ipsum dolor sit amet, consectetur adipisicing elit, sed do eiusmod tempor incididunt ut labore et dolore magna aliqua. Ut enim ad minim veniam, quis nostrud exercitation <span class="hl">ullamco laboris nisi ut aliquip</span> ex ea commodo consequat.</li>
    <li>Duis aute irure dolor in reprehenderit in voluptate velit esse cillum dolore eu fugiat nulla pariatur. Excepteur sint occaecat cupidatat non proident, sunt in culpa qui officia deserunt mollit anim id est laborum.</li>
  </ul>
  <div class="slide-foot"><span class="page-no">Page<b>3</b></span><span class="foot-title">Business presentation for client Northfield</span></div>
</section>

<section class="slide col-c row-1">
  <div class="brand"><span class="brand-name">PALMERA</span></div>
  <div class="section-title">
    <div class="st-name">Project concepts</div>
    <div class="st-sub">Lorem ipsum dolor sit amet</div>
  </div>
</section>

<!-- row 2 -->
<section class="slide col-a row-2">
  <div class="slide-head"><span class="h-title display">Our company</span><span class="h-sub display">Lorem ipsum dolor sit amet</span></div>
  <div class="brand"><span class="brand-name">PALMERA</span></div>
  <div style="position:absolute;left:14px;top:50px;width:4px;height:122px;background:var(--orange)"></div>
  <div class="photo photo-cables" role="img" aria-label="Close-up photo of network cables plugged into a switch" style="left:18px;top:50px;width:124px;height:122px"></div>
  <div class="copy" style="position:absolute;left:148px;top:56px;width:210px">
    <div class="label">History</div>
    <p>Lorem ipsum dolor sit amet, consectetur adipisicing elit, sed do eiusmod tempor incididunt ut labore et dolore magna aliqua. Ut enim ad minim veniam, quis nostrud exercitation ullamco laboris nisi ut aliquip ex ea commodo consequat.</p>
    <div class="label" style="margin-top:24px">Location</div>
    <p>Duis aute irure dolor in reprehenderit in voluptate velit esse cillum dolore eu fugiat nulla pariatur.</p>
    <p>Excepteur sint occaecat cupidatat non proident, sunt in culpa qui officia deserunt mollit anim id est laborum.</p>
  </div>
  <div class="slide-foot"><span class="page-no">Page<b>4</b></span><span class="foot-title">Business presentation for client Northfield</span></div>
</section>

<section class="slide col-b row-2">
  <div class="photo photo-cables" role="img" aria-label="Photo of blue network cables connected to a server" style="left:0;top:0;width:216px;height:212px"></div>
  <div style="position:absolute;left:216px;top:0;width:159px;height:212px;background:var(--dark-panel)"></div>
  <div class="brand" style="left:22px;top:11px"><span class="brand-name">PALMERA</span></div>
  <div class="display" style="position:absolute;right:165px;top:80px;font-size:19px;line-height:33px;color:#fff;text-align:right">Here is what you're<br>looking for!</div>
  <div class="display" style="position:absolute;left:223px;top:89px;font-size:12px;line-height:14px;color:var(--orange)">Our experience shall<br>solve your problems</div>
</section>

<section class="slide col-c row-2">
  <div class="slide-head"><span class="h-title display">3 impressive pillars</span><span class="h-sub display">Lorem ipsum dolor sit amet</span></div>
  <div class="brand"><span class="brand-name">PALMERA</span></div>
  <div class="copy" style="position:absolute;left:20px;top:46px;width:102px">
    <div class="label">Reborn</div>
    <p>Lorem ipsum dolor sit amet, consectetur adipisicing elit, sed do eiusmod tempor incididunt ut labore et dolore magna aliqua. Ut enim ad minim veniam, quis nostrud exercitation ullamco laboris nisi ut aliquip ex ea commodo consequat.</p>
    <p><span class="hl">Duis aute irure</span> dolor in reprehenderit in voluptate velit esse cillum dolore eu fugiat nulla pariatur. Excepteur sint occaecat cupidatat non proident, sunt in culpa qui officia deserunt mollit anim id est laborum.</p>
  </div>
  <div class="copy" style="position:absolute;left:137px;top:46px;width:102px">
    <div class="label">Reunite</div>
    <p><span class="hl">Sed ut perspiciatis,</span> unde omnis iste natus error sit voluptatem accusantium doloremque laudantium, totam rem aperiam eaque ipsa, quae ab illo inventore veritatis et quasi <span class="hl">architecto beatae vitae dicta sunt,</span> explicabo. Nemo enim ipsam voluptatem, quia voluptas sit, aspernatur aut odit aut fugit, sed quia consequuntur magni dolores eos, qui ratione voluptatem sequi nesciunt, neque porro quisquam est, qui dolorem ipsum, quia dolor sit amet consectetur adipisci velit, sed quia non numquam eius modi tempora incidunt, ut labore et dolore magnam aliquam quaerat voluptatem.</p>
  </div>
  <div class="copy" style="position:absolute;left:254px;top:46px;width:102px">
    <div class="label">Reinforce</div>
    <p>At vero eos et accusamus et iusto odio dignissimos ducimus, qui blanditiis praesentium voluptatum deleniti atque corrupti, quos dolores et quas molestias excepturi sint, obcaecati <span class="hl">cupiditate non provident,</span> similique sunt in culpa, qui officia deserunt mollitia animi, id est laborum et dolorum fuga.</p>
    <p><span class="hl">Et harum quidem rerum</span> facilis est et expedita distinctio. Nam libero tempore, cum soluta nobis est eligendi optio, cumque nihil impedit, quo minus id, quod maxime placeat, facere possimus, omnis voluptas assumenda est, omnis dolor repellendus.</p>
  </div>
  <div class="slide-foot"><span class="page-no">Page<b>6</b></span><span class="foot-title">Presentation title here</span></div>
</section>

<!-- row 3 -->
<section class="slide col-a row-3">
  <div class="slide-head"><span class="h-title display">Main concept</span><span class="h-sub display">Lorem ipsum dolor sit amet</span></div>
  <div class="brand"><span class="brand-name">PALMERA</span></div>
  <div class="display orange" style="position:absolute;left:47px;top:133px;font-size:6.5px">Lorem ipsum dolor sit amet</div>
  <div style="position:absolute;left:0;top:144px;width:132px;height:2px;background:var(--orange)"></div>
  <div class="copy" style="position:absolute;left:137px;top:134px;width:222px">
    <p>Lorem ipsum dolor sit amet, consectetur adipisicing elit, sed do eiusmod tempor incididunt ut labore et dolore magna aliqua. Ut enim ad minim veniam, quis nostrud exercitation ullamco laboris nisi ut aliquip ex ea commodo consequat.</p>
    <p>Duis aute irure dolor in reprehenderit in voluptate velit esse cillum dolore eu fugiat nulla pariatur. Excepteur sint occaecat cupidatat non proident, sunt in culpa qui officia deserunt mollit anim id est laborum.</p>
  </div>
  <div class="slide-foot"><span class="page-no">Page<b>8</b></span><span class="foot-title">Presentation title here</span></div>
</section>

<section class="slide col-b row-3">
  <div class="brand"><span class="brand-name">PALMERA</span></div>
  <div class="section-title">
    <div class="st-name">Marketing</div>
    <div class="st-sub">Lorem ipsum dolor sit amet</div>
  </div>
</section>

<section class="slide col-c row-3">
  <div class="photo photo-desk" role="img" aria-label="Photo of an open laptop showing code on a bright desk with a phone and pen" style="left:0;top:0;width:375px;height:212px"></div>
  <div class="brand" style="left:22px;top:11px"><span class="brand-name">PALMERA</span></div>
  <div class="display" style="position:absolute;left:25px;top:80px;font-size:19px;line-height:30px;color:#fff">We provide the<br>best IT solutions</div>
  <div class="display orange" style="position:absolute;left:25px;top:140px;font-size:12px">It's palmera</div>
</section>

<!-- row 4 -->
<section class="slide col-a row-4">
  <div class="slide-head"><span class="h-title display">Our team</span><span class="h-sub display">Lorem ipsum dolor sit amet</span></div>
  <div class="brand"><span class="brand-name">PALMERA</span></div>
  <div class="photo photo-person" role="img" aria-label="Portrait photo of team member Anna Reyes" style="left:18px;top:45px;width:80px;height:78px"></div>
  <div class="photo photo-person" role="img" aria-label="Portrait photo of team member Tom Lindqvist" style="left:105px;top:45px;width:80px;height:78px"></div>
  <div class="photo photo-person" role="img" aria-label="Portrait photo of team member Maya Okafor" style="left:192px;top:45px;width:80px;height:78px"></div>
  <div class="photo photo-person" role="img" aria-label="Portrait photo of team member Leo Brandt" style="left:279px;top:45px;width:80px;height:78px"></div>
  <div class="copy" style="position:absolute;left:18px;top:128px;width:80px"><div class="label">Anna Reyes</div><p>Lorem ipsum dolor sit amet, consectetur adipisicing elit, sed do eiusmod tempor incididunt ut labore et dolore magna aliqua.</p></div>
  <div class="copy" style="position:absolute;left:105px;top:128px;width:80px"><div class="label">Tom Lindqvist</div><p>Duis aute irure dolor in reprehenderit in voluptate velit esse cillum dolore eu fugiat nulla pariatur.</p></div>
  <div class="copy" style="position:absolute;left:192px;top:128px;width:80px"><div class="label">Maya Okafor</div><p>Lorem ipsum dolor sit amet, consectetur adipisicing elit, sed do eiusmod tempor incididunt ut labore et dolore magna aliqua.</p></div>
  <div class="copy" style="position:absolute;left:279px;top:128px;width:80px"><div class="label">Leo Brandt</div><p>Duis aute irure dolor in reprehenderit in voluptate velit esse cillum dolore eu fugiat nulla pariatur.</p></div>
  <div class="slide-foot"><span class="page-no">Page<b>9</b></span><span class="foot-title">Presentation title here</span></div>
</section>

<section class="slide col-b row-4">
  <div class="slide-head"><span class="h-title display">How to enlarge our market</span><span class="h-sub display">Lorem ipsum dolor sit amet</span></div>
  <div class="brand"><span class="brand-name">PALMERA</span></div>
  <div class="photo photo-servers" role="img" aria-label="Photo of server cabinets in a data centre" style="left:30px;top:45px;width:142px;height:80px"></div>
  <div class="photo photo-rack" role="img" aria-label="Photo of patch cables in a server rack with status lights" style="left:199px;top:45px;width:142px;height:80px"></div>
  <div class="copy" style="position:absolute;left:30px;top:129px;width:142px"><div class="label">Project # 1 client Northfield</div><p>Lorem ipsum dolor sit amet, consectetur adipisicing elit, sed do eiusmod tempor incididunt ut labore et dolore magna aliqua.</p><p>Ut enim ad minim veniam, quis nostrud exercitation ullamco laboris nisi ut aliquip ex ea commodo consequat.</p></div>
  <div class="copy" style="position:absolute;left:199px;top:129px;width:142px"><div class="label">Project # 2 client Southbay</div><p>Duis aute irure dolor in reprehenderit in voluptate velit esse cillum dolore eu fugiat nulla pariatur.</p><p>Excepteur sint occaecat cupidatat non proident, sunt in culpa qui officia deserunt mollit anim id est laborum.</p></div>
  <div class="slide-foot"><span class="page-no">Page<b>10</b></span><span class="foot-title">Presentation title here</span></div>
</section>

<section class="slide col-c row-4">
  <div class="slide-head"><span class="h-title display">Two column text</span><span class="h-sub display">More details here</span></div>
  <div class="brand"><span class="brand-name">PALMERA</span></div>
  <div class="copy" style="position:absolute;left:22px;top:37px;width:162px;text-align:justify">
    <p>Sed ut perspiciatis, unde omnis iste natus error sit voluptatem accusantium doloremque laudantium, totam rem aperiam eaque ipsa, quae ab illo inventore veritatis et quasi architecto beatae vitae dicta sunt, explicabo. Nemo enim ipsam voluptatem, quia voluptas sit, aspernatur aut odit aut fugit, <span class="hl">sed quia consequuntur magni dolores eos,</span> qui ratione voluptatem sequi nesciunt, neque porro quisquam est, qui dolorem ipsum, quia dolor sit amet consectetur adipisci velit, sed quia non numquam eius modi tempora incidunt, ut labore et dolore magnam aliquam quaerat voluptatem.</p>
    <p><span class="hl">Ut enim ad minima veniam, quis nostrum</span> exercitationem ullam corporis suscipit laboriosam, nisi ut aliquid ex ea commodi consequatur?</p>
    <p>Sed ut perspiciatis, unde omnis iste natus error sit voluptatem accusantium doloremque laudantium, totam rem aperiam eaque ipsa, quae ab illo inventore veritatis et quasi architecto beatae vitae dicta sunt, explicabo.</p>
    <p>Nemo enim ipsam voluptatem, quia voluptas sit, aspernatur aut odit aut fugit, sed quia consequuntur magni dolores eos, qui ratione voluptatem sequi nesciunt, neque porro quisquam est, qui dolorem ipsum, quia dolor sit amet consectetur adipisci velit, sed quia non numquam eius modi tempora incidunt, ut labore et dolore.</p>
  </div>
  <div class="copy" style="position:absolute;left:193px;top:37px;width:162px;text-align:justify">
    <p>Magnam aliquam quaerat voluptatem.</p>
    <p>Ut enim ad minima veniam, quis nostrum exercitationem ullam corporis suscipit laboriosam, nisi ut aliquid ex ea commodi consequatur?</p>
    <p>Ut enim ad minima veniam, quis nostrum exercitationem ullam corporis suscipit laboriosam, nisi ut aliquid ex ea commodi consequatur? Sed ut perspiciatis, unde omnis iste natus error sit voluptatem accusantium doloremque laudantium, totam rem aperiam eaque ipsa, quae ab illo inventore veritatis et quasi architecto beatae vitae dicta sunt, explicabo.</p>
    <p>Nemo enim ipsam voluptatem, quia voluptas sit, aspernatur aut odit aut fugit, sed quia consequuntur magni dolores eos, qui ratione voluptatem sequi nesciunt, neque porro quisquam est, qui dolorem ipsum, quia dolor sit amet consectetur adipisci velit, sed quia non numquam eius modi tempora incidunt, ut labore et dolore.</p>
    <p>Ut enim ad minima veniam, quis nostrum exercitationem ullam corporis suscipit laboriosam, nisi ut aliquid ex ea commodi consequatur?</p>
  </div>
  <div class="slide-foot"><span class="page-no">Page<b>16</b></span><span class="foot-title">Presentation title here</span></div>
</section>

<!-- row 5 -->
<section class="slide col-a row-5">
  <div class="slide-head"><span class="h-title display">Data slides</span><span class="h-sub display">Your data info here</span></div>
  <div class="brand"><span class="brand-name">PALMERA</span></div>
  <svg style="position:absolute;left:28px;top:55px" width="200" height="110" viewBox="0 0 200 110" aria-label="Bar chart comparing April, May and June">
    <g font-family="Open Sans,sans-serif" font-size="3.5" fill="#777" text-anchor="end">
      <text x="10" y="10">70</text><text x="10" y="27">56</text><text x="10" y="44">42</text><text x="10" y="61">28</text><text x="10" y="78">14</text><text x="10" y="95">0</text>
    </g>
    <rect x="27" y="70" width="28" height="25" fill="#3d8ad6"/>
    <rect x="55" y="33" width="28" height="62" fill="#f26a10"/>
    <rect x="83" y="60" width="26" height="35" fill="#3d8ad6"/>
    <rect x="109" y="45" width="28" height="50" fill="#f26a10"/>
    <rect x="137" y="36" width="26" height="59" fill="#3d8ad6"/>
    <rect x="163" y="14" width="26" height="81" fill="#f26a10"/>
    <line x1="14" y1="95" x2="195" y2="95" stroke="#bbb" stroke-width=".5"/>
    <g font-family="Open Sans,sans-serif" font-size="3.5" fill="#555" text-anchor="middle">
      <text x="55" y="101">APRIL</text><text x="109" y="101">MAY</text><text x="163" y="101">JUNE</text>
    </g>
  </svg>
  <div style="position:absolute;left:223px;top:74px;width:135px">
    <div class="display" style="font-size:6.5px;line-height:8px;color:#3d3d3d">We will help you grow your idea<br>into a profitable business</div>
    <div class="display" style="font-size:4.5px;color:#555;margin-top:5px">Nascetur ridiculus mus maecenas nunc nisi eros dolentis</div>
    <div class="display" style="font-size:4.2px;line-height:6px;color:#777;margin-top:5px">Reprehenderit in voluptate velit esse cillum dolore magna sunt, simul cum quo voluptatem deserunt omnibus leo magna et dolore, erat purus, vivamus enim lorem ipsum sed commodo nibh dolor sit amet, sed eiusmod tempor</div>
  </div>
  <div class="slide-foot"><span class="page-no">Page<b>14</b></span><span class="foot-title">Presentation title here</span></div>
</section>

<section class="slide col-b row-5">
  <div class="slide-head"><span class="h-title display">Data slides</span><span class="h-sub display">Your data info here</span></div>
  <div class="brand"><span class="brand-name">PALMERA</span></div>
  <div class="display" style="position:absolute;left:20px;top:42px;font-size:5.5px;color:#333;font-weight:400">Asia market</div>
  <div class="display" style="position:absolute;left:20px;top:50px;font-size:20px;color:var(--slate)">$23M</div>
  <p class="copy" style="position:absolute;left:20px;top:78px;width:160px;color:#999">Of shopping carts are abandoned right before the transaction its completed. Suitable for all categories in the businesses</p>
  <div class="display" style="position:absolute;left:197px;top:42px;font-size:5.5px;color:#333;font-weight:400">USA market</div>
  <div class="display" style="position:absolute;left:197px;top:50px;font-size:20px;color:var(--slate)">$27M</div>
  <p class="copy" style="position:absolute;left:197px;top:78px;width:160px;color:#999">Of shopping carts are abandoned right before the transaction its completed. Suitable for all categories in the businesses</p>
  <svg style="position:absolute;left:14px;top:98px" width="350" height="90" viewBox="0 0 350 90" aria-label="Stacked bar charts for Asia and USA markets">
    <g font-family="Open Sans,sans-serif" font-size="2.8" fill="#777" text-anchor="end">
      <text x="22" y="12">Marketing</text><text x="22" y="27">SEO Analytics</text><text x="22" y="42">Web Design</text><text x="22" y="57">Graphic Design</text>
      <text x="199" y="12">Marketing</text><text x="199" y="27">SEO Analytics</text><text x="199" y="42">Web Design</text><text x="199" y="57">Graphic Design</text>
    </g>
    <g>
      <rect x="25" y="8" width="40" height="5" fill="#4a5468"/><rect x="65" y="8" width="70" height="5" fill="#f26a10"/><rect x="135" y="8" width="45" height="5" fill="#aaa"/>
      <rect x="25" y="23" width="60" height="5" fill="#4a5468"/><rect x="85" y="23" width="45" height="5" fill="#f26a10"/><rect x="130" y="23" width="50" height="5" fill="#aaa"/>
      <rect x="25" y="38" width="55" height="5" fill="#4a5468"/><rect x="80" y="38" width="50" height="5" fill="#f26a10"/><rect x="130" y="38" width="50" height="5" fill="#aaa"/>
      <rect x="25" y="53" width="38" height="5" fill="#4a5468"/><rect x="63" y="53" width="32" height="5" fill="#f26a10"/><rect x="95" y="53" width="85" height="5" fill="#aaa"/>
      <rect x="202" y="8" width="40" height="5" fill="#4a5468"/><rect x="242" y="8" width="70" height="5" fill="#f26a10"/><rect x="312" y="8" width="34" height="5" fill="#aaa"/>
      <rect x="202" y="23" width="60" height="5" fill="#4a5468"/><rect x="262" y="23" width="45" height="5" fill="#f26a10"/><rect x="307" y="23" width="39" height="5" fill="#aaa"/>
      <rect x="202" y="38" width="55" height="5" fill="#4a5468"/><rect x="257" y="38" width="50" height="5" fill="#f26a10"/><rect x="307" y="38" width="39" height="5" fill="#aaa"/>
      <rect x="202" y="53" width="38" height="5" fill="#4a5468"/><rect x="240" y="53" width="32" height="5" fill="#f26a10"/><rect x="272" y="53" width="74" height="5" fill="#aaa"/>
    </g>
    <g font-family="Open Sans,sans-serif" font-size="2.6" fill="#999" text-anchor="middle">
      <text x="25" y="64">0%</text><text x="70" y="64">25%</text><text x="115" y="64">50%</text><text x="160" y="64">75%</text>
      <text x="202" y="64">0%</text><text x="247" y="64">25%</text><text x="292" y="64">50%</text><text x="337" y="64">75%</text>
    </g>
    <g font-family="Open Sans,sans-serif" font-size="2.8" fill="#777">
      <rect x="158" y="75" width="3" height="3" fill="#4a5468"/><text x="162" y="78">2010</text>
      <rect x="170" y="75" width="3" height="3" fill="#f26a10"/><text x="174" y="78">2014</text>
      <rect x="182" y="75" width="3" height="3" fill="#aaa"/><text x="186" y="78">2015</text>
    </g>
  </svg>
  <div class="slide-foot"><span class="page-no">Page<b>15</b></span><span class="foot-title">Presentation title here</span></div>
</section>

<section class="slide col-c row-5">
  <div class="slide-head"><span class="h-title display">Project plan</span><span class="h-sub display">Lorem ipsum dolor sit amet</span></div>
  <div class="brand"><span class="brand-name">PALMERA</span></div>
  <div class="copy" style="position:absolute;left:20px;top:45px;width:158px">
    <div class="label">Cost estimation</div>
    <p>Sed ut perspiciatis, unde omnis iste natus error sit voluptatem accusantium doloremque laudantium, totam rem aperiam eaque ipsa, quae ab illo inventore veritatis et quasi architecto beatae vitae dicta sunt, explicabo. Nemo enim ipsam voluptatem, quia voluptas sit, aspernatur aut odit aut fugit, <span class="hl">sed quia consequuntur magni dolores eos,</span> qui ratione voluptatem sequi nesciunt, neque porro quisquam est, qui dolorem ipsum, quia dolor sit amet consectetur adipisci velit, sed quia non numquam eius modi tempora incidunt, ut labore et dolore magnam aliquam quaerat voluptatem.</p>
    <p><span class="hl">Ut enim ad minima veniam, quis nostrum</span> exercitationem ullam corporis suscipit laboriosam, nisi ut aliquid ex ea commodi consequatur?</p>
  </div>
  <div class="copy" style="position:absolute;left:189px;top:45px;width:158px">
    <div class="label">Fix the schedule</div>
    <p>At vero eos et accusamus et iusto odio dignissimos ducimus, qui blanditiis praesentium voluptatum deleniti atque corrupti, quos dolores et <span class="hl">quas molestias excepturi</span> sint, obcaecati cupiditate non provident, similique sunt in culpa, qui officia deserunt mollitia animi, id est laborum et dolorum fuga. Et harum quidem rerum facilis est et expedita distinctio.</p>
    <p><span class="hl">Nam libero tempore,</span> cum soluta nobis est eligendi optio, cumque nihil impedit, quo minus id, quod maxime placeat, facere possimus, omnis voluptas assumenda est, omnis dolor repellendus. Temporibus autem quibusdam et aut officiis debitis aut rerum necessitatibus saepe eveniet, ut <span class="hl">et voluptates repudiandae sint</span> et molestiae non recusandae. Itaque earum rerum hic tenetur a sapiente delectus, ut aut reiciendis voluptatibus maiores alias consequatur aut perferendis doloribus asperiores repellat.</p>
  </div>
  <div class="slide-foot"><span class="page-no">Page<b>17</b></span><span class="foot-title">Presentation title here</span></div>
</section>

<!-- row 6 -->
<section class="slide col-a row-6">
  <div class="slide-head"><span class="h-title display">Sales and purchases</span><span class="h-sub display">Lorem ipsum dolor sit amet</span></div>
  <div class="brand"><span class="brand-name">PALMERA</span></div>
  <svg style="position:absolute;left:14px;top:62px" width="190" height="110" viewBox="0 0 190 110" aria-label="Monthly sales bars with purchases line">
    <g font-family="Open Sans,sans-serif" font-size="3.5" fill="#777" text-anchor="end">
      <text x="10" y="8">120</text><text x="10" y="22">100</text><text x="10" y="36">80</text><text x="10" y="50">60</text><text x="10" y="64">40</text><text x="10" y="78">20</text><text x="10" y="92">0</text>
    </g>
    <g fill="#aaa">
      <rect x="15" y="57" width="8" height="33"/><rect x="29" y="53" width="8" height="37"/><rect x="43" y="64" width="8" height="26"/><rect x="57" y="55" width="8" height="35"/>
      <rect x="71" y="69" width="8" height="21"/><rect x="85" y="46" width="8" height="44"/><rect x="99" y="52" width="8" height="38"/><rect x="113" y="43" width="8" height="47"/>
      <rect x="127" y="32" width="8" height="58"/><rect x="141" y="36" width="8" height="54"/><rect x="155" y="28" width="8" height="62"/><rect x="169" y="24" width="8" height="66"/>
    </g>
    <polyline fill="none" stroke="#f26a10" stroke-width="1" points="19,48 33,52 47,42 61,58 75,61 89,58 103,50 117,38 131,40 145,28 159,34 173,26"/>
    <g fill="#f26a10"><circle cx="19" cy="48" r="1.3"/><circle cx="33" cy="52" r="1.3"/><circle cx="47" cy="42" r="1.3"/><circle cx="61" cy="58" r="1.3"/><circle cx="75" cy="61" r="1.3"/><circle cx="89" cy="58" r="1.3"/><circle cx="103" cy="50" r="1.3"/><circle cx="117" cy="38" r="1.3"/><circle cx="131" cy="40" r="1.3"/><circle cx="145" cy="28" r="1.3"/><circle cx="159" cy="34" r="1.3"/><circle cx="173" cy="26" r="1.3"/></g>
    <g font-family="Open Sans,sans-serif" font-size="3" fill="#555" text-anchor="middle">
      <text x="19" y="97">JAN</text><text x="33" y="97">FEB</text><text x="47" y="97">MAR</text><text x="61" y="97">APR</text><text x="75" y="97">MAY</text><text x="89" y="97">JUN</text><text x="103" y="97">JUL</text><text x="117" y="97">AUG</text><text x="131" y="97">SEP</text><text x="145" y="97">OCT</text><text x="159" y="97">NOV</text><text x="173" y="97">DEC</text>
    </g>
    <g font-family="Open Sans,sans-serif" font-size="2.8" fill="#555">
      <rect x="70" y="102" width="3" height="3" fill="#aaa"/><text x="74" y="105">SALES</text>
      <line x1="87" y1="103.5" x2="93" y2="103.5" stroke="#f26a10" stroke-width="1"/><text x="94" y="105">PURCHASES</text>
    </g>
  </svg>
  <div class="copy" style="position:absolute;left:211px;top:62px;width:150px">
    <div class="label">Sales</div>
    <p>Lorem ipsum dolor sit amet, consectetur adipisicing elit, sed do eiusmod tempor <span class="hl">incididunt ut labore</span> et dolore magna aliqua. Ut enim ad minim veniam, quis nostrud exercitation ullamco laboris nisi ut aliquip ex ea commodo consequat.</p>
    <p>Duis aute irure dolor in <span class="hl">reprehenderit in voluptate</span> velit esse cillum dolore eu fugiat nulla pariatur. Excepteur sint occaecat cupidatat non proident, sunt in culpa qui officia deserunt mollit anim id est laborum.</p>
  </div>
  <div class="slide-foot"><span class="page-no">Page<b>13</b></span><span class="foot-title">Presentation title here</span></div>
</section>

<section class="slide col-b row-6">
  <div class="slide-head"><span class="h-title display">Positive? Negative?</span><span class="h-sub display">Lorem ipsum dolor sit amet</span></div>
  <div class="brand"><span class="brand-name">PALMERA</span></div>
  <svg style="position:absolute;left:0;top:38px" width="375" height="64" viewBox="0 0 375 64" aria-label="Donut charts: Tokyo 78%, Paris 90%, New York 86%">
    <g fill="none" stroke-width="6">
      <circle cx="71" cy="31" r="24" stroke="#8a8a8a"/>
      <circle cx="71" cy="31" r="24" stroke="#f26a10" stroke-dasharray="117.6 150.8" transform="rotate(-90 71 31)"/>
      <circle cx="187" cy="31" r="24" stroke="#8a8a8a"/>
      <circle cx="187" cy="31" r="24" stroke="#f26a10" stroke-dasharray="135.7 150.8" transform="rotate(-90 187 31)"/>
      <circle cx="304" cy="31" r="24" stroke="#8a8a8a"/>
      <circle cx="304" cy="31" r="24" stroke="#f26a10" stroke-dasharray="129.7 150.8" transform="rotate(-90 304 31)"/>
    </g>
    <g font-family="Oswald,sans-serif" font-weight="300" font-size="15" fill="#333" text-anchor="middle">
      <text x="71" y="37">78%</text><text x="187" y="37">90%</text><text x="304" y="37">86%</text>
    </g>
  </svg>
  <div class="copy" style="position:absolute;left:32px;top:125px;width:78px"><div class="label">Tokyo</div><p>Lorem ipsum dolor sit amet, consectetur adipisicing elit, sed do eiusmod tempor incididunt ut labore et dolore magna aliqua.</p></div>
  <div class="copy" style="position:absolute;left:148px;top:125px;width:78px"><div class="label">Paris</div><p>Duis aute irure dolor in reprehenderit in voluptate velit esse cillum dolore eu fugiat nulla pariatur.</p></div>
  <div class="copy" style="position:absolute;left:265px;top:125px;width:78px"><div class="label">New York</div><p>Lorem ipsum dolor sit amet, consectetur adipisicing elit, sed do eiusmod tempor incididunt ut labore et dolore magna aliqua.</p></div>
  <div class="slide-foot"><span class="page-no">Page<b>12</b></span><span class="foot-title">Presentation title here</span></div>
</section>

<section class="slide col-c row-6">
  <div class="brand"><span class="brand-name">PALMERA</span></div>
  <div class="poster" style="position:absolute;left:25px;top:86px;font-size:44px;line-height:1;color:#3d3d3d">Thank you!</div>
  <div class="display orange" style="position:absolute;left:25px;top:127px;font-size:11px">Any questions?</div>
</section>

</body>
</html>
```